Mindfulness School for Children -- Business Cards

We're looking for business cards for our school directors and owners. We're a mindfulness school for children called tumbling willows. Attached are our logos/icons.

```html
<!DOCTYPE html>
<html lang="en">
<head>
<meta charset="utf-8">
<title>Tumbling Willows – Business Cards</title>
<link rel="stylesheet" href="https://fonts.googleapis.com/css2?family=Alegreya:wght@400&family=Barlow:wght@500;700&family=Montserrat:wght@500;600&display=swap">
<style>
  :root {
    --page: #ededed;
    --green: #57b84c;
    --green-mid: #62c08e;
    --sky: #74cce6;
    --teal: #1494b6;
    --white: #ffffff;
    --shadow: rgba(0, 0, 0, 0.28);
  }
  * { box-sizing: border-box; margin: 0; padding: 0; }
  html, body {
    width: 959px; height: 1200px; overflow: hidden;
    background: var(--page);
  }
  .sheet { position: relative; width: 959px; height: 1200px; }

  .card {
    position: absolute;
    box-shadow: 0 1px 4px var(--shadow);
    overflow: hidden;
  }

  /* Front */
  .card-front {
    left: 122px; top: 125px; width: 711px; height: 407px;
    background: linear-gradient(90deg, var(--green) 0%, var(--green-mid) 50%, var(--sky) 100%);
  }
  .front-tab {
    position: absolute; top: 153px; width: 16px; height: 98px;
    background: var(--white);
  }
  .front-tab.left { left: 0; }
  .front-tab.right { right: 0; }
  .front-name {
    position: absolute; left: 0; right: 0; top: 178px;
    text-align: center;
    font-family: "Alegreya", Georgia, serif;
    font-size: 50px; line-height: 1;
    color: var(--white);
  }
  .front-web {
    position: absolute; left: 0; right: 0; top: 353px;
    text-align: center;
    font-family: "Montserrat", Arial, sans-serif;
    font-weight: 600; font-size: 17px; letter-spacing: 2px;
    color: var(--white);
  }

  /* Back */
  .card-back {
    left: 122px; top: 662px; width: 732px; height: 419px;
    background: var(--white);
  }
  .back-panel {
    position: absolute; left: 0; top: 0; width: 202px; height: 100%;
    background: linear-gradient(90deg, var(--green) 0%, var(--green-mid) 55%, var(--sky) 100%);
  }
  .back-name {
    position: absolute; left: 92px; top: 209px;
    transform: translate(-50%, -50%) rotate(-90deg);
    white-space: nowrap;
    font-family: "Alegreya", Georgia, serif;
    font-size: 40px; line-height: 1;
    color: var(--white);
  }
  .contact-rail { position: absolute; left: 0; top: 0; }

  .person-name {
    position: absolute; left: 267px; top: 94px;
    font-family: "Barlow", Arial, sans-serif;
    font-size: 43px; line-height: 1; letter-spacing: 0.5px;
    color: var(--teal);
  }
  .person-name .first { font-weight: 700; }
  .person-name .last { font-weight: 500; }
  .designation {
    position: absolute; left: 268px; top: 143px;
    font-family: "Montserrat", Arial, sans-serif;
    font-weight: 600; font-size: 17px; letter-spacing: 2px;
    color: var(--teal);
  }
  .rule {
    position: absolute; left: 268px; top: 173px; width: 60px; height: 3px;
    background: var(--green);
  }
  .contact-list { list-style: none; }
  .contact-list li {
    position: absolute; left: 267px;
    font-family: "Montserrat", Arial, sans-serif;
    font-weight: 500; font-size: 17px; line-height: 1;
    color: var(--teal);
  }
  .contact-list .address { top: 198px; }
  .contact-list .phone { top: 240px; }
  .contact-list .email { top: 278px; }
  .contact-list .web { top: 314px; left: 270px; }
</style>
</head>
<body>
<main class="sheet">

  <section class="card card-front" aria-label="Business card front">
    <span class="front-tab left"></span>
    <span class="front-tab right"></span>
    <h1 class="front-name">tumbling willows</h1>
    <p class="front-web">www.yourwebsite.com</p>
  </section>

  <section class="card card-back" aria-label="Business card back">
    <div class="back-panel">
      <p class="back-name">tumbling willows</p>
    </div>

    <svg class="contact-rail" width="300" height="419" viewBox="0 0 300 419" aria-hidden="false">
      <circle cx="202" cy="48" r="44" fill="var(--teal)" role="img" aria-label="School emblem area"/>
      <path d="M182 100 H221 V358 L202 378 L182 358 Z" fill="var(--teal)"/>
      <circle cx="202" cy="111" r="32" fill="var(--green)" stroke="var(--white)" stroke-width="0" />
      <circle cx="202" cy="111" r="23" fill="none" stroke="var(--white)" stroke-width="1.2" role="img" aria-label="Profile photo placeholder"/>

      <!-- location pin -->
      <path d="M202 197 a8 8 0 0 1 8 8 c0 6 -8 14 -8 14 s-8 -8 -8 -14 a8 8 0 0 1 8 -8 z" fill="var(--white)"/>
      <circle cx="202" cy="205" r="3" fill="var(--teal)"/>
      <!-- phone -->
      <path d="M195 238 c2 -2 4 -1 5 1 l2 3 c1 2 0 3 -1 4 c1 3 4 6 7 7 c1 -1 2 -2 4 -1 l3 2 c2 1 2 3 1 5 c-2 2 -4 3 -7 2 c-7 -3 -13 -9 -15 -16 c-1 -3 0 -5 1 -7 z" fill="var(--white)"/>
      <!-- envelope -->
      <rect x="191" y="279" width="23" height="15" fill="none" stroke="var(--white)" stroke-width="1.6"/>
      <path d="M191 279 L202.5 289 L214 279 M191 294 L199 286 M214 294 L206 286" fill="none" stroke="var(--white)" stroke-width="1.6"/>
      <!-- cursor -->
      <path d="M198 312 L198 331 L203 326 L207 334 L210 332 L206 325 L213 324 Z" fill="var(--white)"/>
    </svg>

    <h2 class="person-name"><span class="first">NAME</span> <span class="last">SURNAME</span></h2>
    <p class="designation">DESIGNATION</p>
    <span class="rule"></span>

    <ul class="contact-list">
      <li class="address">Your Address Here</li>
      <li class="phone">+00 111 222 78</li>
      <li class="email">hello@tumblingwillows.com</li>
      <li class="web">www.companywebsite.com</li>
    </ul>
  </section>

</main>
</body>
</html>
```